Brightleaf Wellness Website Design

About The Client:
Brightleaf Wellness is a sugar-free foods chain store providing services to Diabetics. They focus on the China domestic market. They describe themselves as being the 3rd space for Diabetics, the space between hospital and the home that help improve the quality of life for people wit Diabetes (see attached infographics).

They regularly hold education and advice events throughout the China. Brightleaf Wellness distribute a wide product range of food that is suitable for diabetic people. Brightleaf Wellness operate as a Franchise, providing business development services and Industry knowledge. They are actively seeking business partnerships at present.

The Brief:
Design a Home page and secondary information page(PSD only no code) that communicates our company services and company philosophy(3rd Space).
The final design should communicate 'Health, Social Responsibility and Professionalism'.
Colour scheme should orientate around Blue and White, see attached logo.

Websites we like:

http://link.venomira.com/home/

https://www.paxtunel.com/

http://dev.zorvik.com/
Updates

Hello all, the client has advised us that he want to display the professional advice service available for diabetic people more so than a food distributor. The client is also hoping to use his website as a marketing platform to attract affiliates and build partnerships as part of Brightleaf Wellness's business expansion strategy.

So can you make the page more corporate, reliable and professional. Use images of experts/doctors interacting with patients and also training/knowledge transfer images.

Thanks

Hello all, could you include stock images of both Chinese and Caucasians

Yeaahhh, Infographics and photos have been uploaded. Feel free to use them in your designs and also as references.

Target Market(s)

The target market is Chinese B2B in the Diabetics industry and Entrepreneurs looking to cooperate with Brightleaf Wellness.

Industry/Entity Type

Education

Requirements
Must have
• menu navigation with 7-8 sections,
a full screen background image,
Social Media icons,
Logo in top left,
Site search.
Nice to have
• The website must be clear and easy to use, less complicated.

See attached files of some Brightleaf Wellness infographics. Feel free to include elements of these into the design.
Should not have
• Should not use stock images of people from any other country, the client wants stock images of Chinese people only. Avoid photos showing obesity.

```html
<!DOCTYPE html>
<html lang="en">
<head>
<meta charset="utf-8">
<title>Brightleaf Wellness — Home</title>
<link rel="stylesheet" href="https://fonts.googleapis.com/css2?family=Open+Sans:wght@400;600;700&family=Kaushan+Script&display=swap">
<style>
:root{
  --blue:#2b8fd6;
  --blue-dark:#1f5f95;
  --red:#e2252b;
  --ink:#333;
  --muted:#666;
  --line:#e3e3e3;
  --footer:#2e2e2e;
  --footer-base:#1f1f1f;
  --footer-text:#b8b8b8;
}
*{box-sizing:border-box;margin:0;padding:0}
html,body{width:900px;height:1200px;overflow:hidden}
body{font-family:"Open Sans",Arial,sans-serif;color:var(--ink);background:#fff;position:relative}
a{color:inherit;text-decoration:none}

/* header */
.site-header{position:absolute;left:0;top:0;width:900px;height:120px;border-bottom:1px solid var(--line)}
.brand{position:absolute;left:42px;top:30px;display:flex;align-items:center;gap:10px}
.brand-square{width:40px;height:40px;background:var(--red)}
.brand-name{font-size:18px;font-weight:700;color:var(--red);line-height:1}
.main-nav{position:absolute;left:292px;top:48px;display:flex;align-items:center}
.main-nav a{font-size:12px;padding:8px 11px;color:var(--ink)}
.main-nav a.active{background:var(--blue);color:#fff}
.header-phone{position:absolute;right:42px;top:53px;display:flex;align-items:center;gap:6px;color:var(--red);font-size:13px;font-weight:600}

/* hero */
.hero{position:absolute;left:0;top:120px;width:900px;height:340px;background:linear-gradient(90deg,#cfdbe4 0%,#e9eef1 45%,#dfe6ea 70%,#c8d3db 100%)}
.hero-intro{position:absolute;left:40px;top:80px;width:330px;background:rgba(43,143,214,.82);padding:14px 18px 18px;color:#fff}
.hero-title{font-family:"Kaushan Script",cursive;font-size:30px;font-weight:400;line-height:1.15;margin-bottom:10px}
.hero-text{font-size:12px;line-height:1.5}
.btn-red{display:inline-block;background:var(--red);color:#fff;font-size:12px;padding:8px 16px;margin-top:14px}

/* services */
.services{position:absolute;left:45px;top:482px;width:810px}
.section-title{text-align:center;font-size:27px;font-weight:400;color:var(--blue-dark);line-height:1.3}
.section-title span{color:var(--blue)}
.service-grid{display:flex;gap:30px;margin-top:16px}
.service-card{width:250px}
.service-photo{position:relative;height:125px}
.view-more{position:absolute;left:0;bottom:0;background:var(--blue);color:#fff;font-size:10px;padding:3px 8px}
.service-title{font-size:15px;font-weight:600;margin:9px 0 5px;line-height:1.3}
.service-title.accent{color:var(--red)}
.service-text{font-size:11px;line-height:1.5;color:var(--muted)}

/* about + testimonials */
.about{position:absolute;left:45px;top:780px;width:250px}
.sub-title{font-size:16px;font-weight:600;color:var(--blue-dark);padding-bottom:7px;border-bottom:2px solid var(--line);line-height:1.3}
.about-body{margin-top:12px;font-size:11px;line-height:1.5;color:var(--muted)}
.about-photo{float:left;width:115px;height:95px;margin:0 10px 4px 0}
.testimonials{position:absolute;left:335px;top:780px;width:520px}
.quote-box{margin-top:12px;border:1px solid var(--line);padding:12px 14px;background:#fafafa}
.quote-meta{display:flex;justify-content:space-between;font-size:11px}
.quote-author{font-weight:700;color:var(--ink)}
.quote-author em{font-style:normal;color:var(--red);font-weight:600}
.quote-date{color:#999}
.quote-text{margin-top:8px;font-size:11px;line-height:1.5;color:var(--muted)}
.quote-foot{display:flex;justify-content:space-between;align-items:center;margin-top:10px}
.dots{display:flex;gap:5px}
.dots i{width:7px;height:7px;border-radius:50%;background:#ccc}
.dots i.on{background:var(--blue)}
.btn-blue{background:var(--blue);color:#fff;font-size:10px;padding:5px 10px}

/* footer */
.site-footer{position:absolute;left:0;top:1005px;width:900px;height:165px;background:var(--footer);color:var(--footer-text);display:flex;padding:16px 45px 0;gap:30px}
.footer-col h4{color:#fff;font-size:13px;font-weight:600;margin-bottom:10px}
.col-sitemap{width:120px}
.col-news{width:215px}
.col-newsletter{width:200px}
.col-social{width:170px}
.footer-list li{list-style:none;font-size:11px;line-height:1.7}
.news-item{display:flex;gap:8px;margin-bottom:10px}
.news-thumb{width:34px;height:34px;flex:none;background:linear-gradient(135deg,#8aa3b5,#c9d3da)}
.news-item p{font-size:10px;line-height:1.45}
.news-item strong{color:var(--blue);font-weight:600}
.newsletter-text{font-size:10px;line-height:1.45;margin-bottom:8px}
.field{display:block;width:100%;height:20px;background:#fff;margin-bottom:6px;font-size:10px;color:#999;padding:3px 6px}
.btn-submit{display:inline-block;background:var(--blue);color:#fff;font-size:10px;padding:4px 12px}
.social-item{display:flex;align-items:center;gap:8px;font-size:11px;margin-bottom:8px}
.social-item i{width:18px;height:18px;flex:none}
.footer-base{position:absolute;left:0;top:1170px;width:900px;height:30px;background:var(--footer-base);color:#888;font-size:10px;text-align:center;line-height:30px}
</style>
</head>
<body>

<header class="site-header">
  <a class="brand" href="#">
    <span class="brand-square"></span>
    <span class="brand-name">Brightleaf Wellness</span>
  </a>
  <nav class="main-nav">
    <a class="active" href="#">Home</a>
    <a href="#">Information</a>
    <a href="#">Philosophy</a>
    <a href="#">Company Services</a>
    <a href="#">Contact Us</a>
  </nav>
  <div class="header-phone">
    <svg width="14" height="14" viewBox="0 0 24 24" aria-hidden="true"><path fill="#e2252b" d="M6.6 10.8a15 15 0 0 0 6.6 6.6l2.2-2.2c.3-.3.7-.4 1-.2 1.1.4 2.3.6 3.6.6.6 0 1 .4 1 1V20c0 .6-.4 1-1 1A17 17 0 0 1 3 4c0-.6.4-1 1-1h3.5c.6 0 1 .4 1 1 0 1.3.2 2.5.6 3.6.1.3 0 .7-.2 1z"/></svg>
    800-5550-147
  </div>
</header>

<section class="hero" role="img" aria-label="Smiling doctor in a white coat in a bright clinic">
  <div class="hero-intro">
    <h1 class="hero-title">Welcome to Brightleaf Wellness</h1>
    <p class="hero-text">Lorem Ipsum is simply dummy text of the printing and typesetting industry. Lorem Ipsum has been the industry's standard dummy text ever since the 1500s, when an unknown printer took a galley of type and scrambled.</p>
    <a class="btn-red" href="#">Learn More &raquo;</a>
  </div>
</section>

<section class="services">
  <h2 class="section-title"><span>+</span> Our Services</h2>
  <div class="service-grid">
    <article class="service-card">
      <div class="service-photo" role="img" aria-label="Doctor with a patient in a consultation room" style="background:linear-gradient(135deg,#9fb8c9,#e4ebef)"><span class="view-more">View More &raquo;</span></div>
      <h3 class="service-title">Health</h3>
      <p class="service-text">Lorem Ipsum is simply dummy text of the printing and typesetting industry. Lorem Ipsum has been the industry's standard dummy text ever since the 1500s.</p>
    </article>
    <article class="service-card">
      <div class="service-photo" role="img" aria-label="Nurse helping an elderly patient" style="background:linear-gradient(135deg,#c9d9e4,#f0e6e0)"><span class="view-more">View More &raquo;</span></div>
      <h3 class="service-title accent">Social Responsibility</h3>
      <p class="service-text">Lorem Ipsum is simply dummy text of the printing and typesetting industry. Lorem Ipsum has been the industry's standard dummy text ever since the 1500s.</p>
    </article>
    <article class="service-card">
      <div class="service-photo" role="img" aria-label="Medical team in a training session" style="background:linear-gradient(135deg,#b3c8d6,#e9eef2)"><span class="view-more">View More &raquo;</span></div>
      <h3 class="service-title">Professionalism</h3>
      <p class="service-text">Lorem Ipsum is simply dummy text of the printing and typesetting industry. Lorem Ipsum has been the industry's standard dummy text ever since the 1500s.</p>
    </article>
  </div>
</section>

<section class="about">
  <h2 class="sub-title">About Brightleaf Wellness</h2>
  <div class="about-body">
    <div class="about-photo" role="img" aria-label="Doctor reviewing notes at a desk" style="background:linear-gradient(135deg,#a9c0d0,#e6ecf0)"></div>
    <p>Lorem Ipsum is simply dummy text of the printing and typesetting industry. Lorem Ipsum has been the industry's standard dummy text ever since the 1500s, when an unknown printer took a galley of type.</p>
  </div>
</section>

<section class="testimonials">
  <h2 class="sub-title">What Our Customers Say</h2>
  <blockquote class="quote-box">
    <div class="quote-meta">
      <span class="quote-author">Liam Carver, <em>Manager</em></span>
      <span class="quote-date">Posted: 15 Jan 2013</span>
    </div>
    <p class="quote-text">Lorem ipsum dolor sit amet, consectetur adipiscing elit. Sed posuere felis quis turpis varius tincidunt in in ipsum. Morbi eget nunc vel nisi commodo facilisis at id mauris. Nam lorem justo, malesuada a rutrum quis, pretium vitae libero. Integer tincidunt blandit consectetur, sit amet fermentum nibh. Mauris ut massa in nisl ullamcorper venenatis.</p>
    <div class="quote-foot">
      <div class="dots"><i class="on"></i><i></i><i></i><i></i></div>
      <a class="btn-blue" href="#">view all testimonials</a>
    </div>
  </blockquote>
</section>

<footer class="site-footer">
  <div class="footer-col col-sitemap">
    <h4>Site Map</h4>
    <ul class="footer-list">
      <li>Home</li><li>Information</li><li>Philosophy</li><li>Company Services</li><li>Contact Us</li>
    </ul>
  </div>
  <div class="footer-col col-news">
    <h4>News</h4>
    <div class="news-item">
      <div class="news-thumb" role="img" aria-label="News thumbnail photo"></div>
      <p><strong>Nora Whitfield</strong> — New care events open for spring, join our team at a local store.</p>
    </div>
    <div class="news-item">
      <div class="news-thumb" role="img" aria-label="News thumbnail photo"></div>
      <p><strong>Nora Whitfield</strong> — Partner program expands to new cities across the region.</p>
    </div>
  </div>
  <div class="footer-col col-newsletter">
    <h4>Newsletter</h4>
    <p class="newsletter-text">Enter your name and email address if you want to receive our newsletter</p>
    <span class="field">Name</span>
    <span class="field">Email</span>
    <a class="btn-submit" href="#">Submit</a>
  </div>
  <div class="footer-col col-social">
    <h4>Social Networks</h4>
    <div class="social-item"><i style="background:#3b5a98"></i>Like us on Pagebook</div>
    <div class="social-item"><i style="background:#29a9e1"></i>Follow us on Chirper</div>
    <div class="social-item"><i style="background:#d2402f"></i>Add us on Circlenet</div>
    <div class="social-item"><i style="background:#1a79b4"></i>Join us on Workline</div>
  </div>
</footer>
<div class="footer-base">Copyright Brightleaf Wellness 2013. All rights reserved.</div>

</body>
</html>
```